Book Cover Design for Millennial

I need a book cover design for my book Sunward Ledger. The subtitle of the book is Seven Quiet Steps Toward Steady Ground at Work.

I'm a career coach who helps millennial career professionals. I myself am a millennial but on the older end (34). I've dealt and been through most of the challenges millennials are facing as career professionals and I wrote this book with the thought of providing guidance and aid to getting past those challenges and shedding light on fundamental habits and practices that will help them excel in their careers. In addition, the book will help them prepare millennials for our turn as the leaders, managers, etc moving forward in corporate America. The final design should have the main title of the book in it as the focal point but not the subtitle. I want the cover to communicate something NEW, Bold, Youthful, non-traditional. I want it to stick out while still maintaining a sleek and Professional look.
Updates

Hello, Designers! I want to thank you all for your submissions! The work is amazing and I greatly appreciate it. If you would I want to help out in this process by adding a few updates based on the submissions I have seen. The concept I think that is coming close to hitting the mark is Bramble Forja. What I would like to see changed about the concept is the following: Change the outfits to be more Millennial Career Professional. I have attached some ideas to the brief. I want to replace this picture with one of multiple millennials anywhere from 3 and up. I would like the pic to have diversity in it representing most races of people in the USA. I would like my name beneath sunward ledger. I'm not a known author yet so having my name that big my distract from the title of the book. Can we make the title a little bigger and so far I like the background.Thanks, DP Added Friday, September 30, 2016

Target Market(s)

Millennial Career Professionals (18 - 34 age group)

Industry/Entity Type

Life Coaching

Logo Text

Sunward Ledger

Requirements
Must have
• communicate something NEW, Bold, Youthful, non-traditional. I want it to stick out while still maintaining a sleek and Professional look.
Nice to have
• something that goes with my brand
• http://www.doranpelwick.com
Should not have
• Nothing 3D or a logo that is hard to read when placed on stationeries, business cards etc

```html
<!DOCTYPE html>
<html lang="en">
<head>
<meta charset="utf-8">
<title>Sunward Ledger — Book Cover</title>
<link rel="stylesheet" href="https://fonts.googleapis.com/css2?family=Open+Sans:wght@400;700;800&family=Montserrat:wght@600;700&display=swap">
<style>
  :root{
    --ink:#111111;
    --title-blue:#1a8ad8;
    --accent-blue:#2a9ee0;
    --spine-blue:#6aaed0;
    --band-blue:#4fb0e6;
    --label-blue:#4aa6e0;
    --sky-deep:#7cc0dc;
    --sky-light:#cfe9f4;
    --paper:#ffffff;
    --text-dark:#333333;
    --photo-grey:#bdbdbd;
  }
  html,body{margin:0;padding:0;overflow:hidden;background:var(--paper);}
  .cover{position:relative;width:1200px;height:794px;overflow:hidden;background:var(--paper);font-family:"Open Sans",sans-serif;}
  .sky{position:absolute;left:0;top:0;width:1200px;height:420px;
    background:linear-gradient(180deg,var(--sky-deep) 0%,var(--sky-light) 45%,rgba(255,255,255,0) 100%);}
  .author-photo{position:absolute;left:34px;top:222px;width:186px;height:248px;
    background:linear-gradient(180deg,#9a9a9a 0%,#d6d6d6 55%,#8c8c8c 100%);
    border-radius:40px 40px 4px 4px;}
  .about-label{position:absolute;left:42px;top:464px;width:178px;height:40px;background:var(--label-blue);
    transform:rotate(-3deg);display:flex;align-items:center;justify-content:center;
    font-family:"Montserrat",sans-serif;font-weight:700;font-size:16px;color:var(--ink);letter-spacing:.5px;}
  .spine{position:absolute;left:564px;top:0;width:72px;height:794px;background:var(--spine-blue);}
  .spine-title{position:absolute;left:12px;top:52px;writing-mode:vertical-rl;font-size:40px;line-height:48px;white-space:nowrap;}
  .spine-title b{font-weight:700;color:var(--ink);}
  .spine-title span{font-weight:400;color:var(--paper);}
  .spine-author{position:absolute;left:26px;top:534px;writing-mode:vertical-rl;white-space:nowrap;font-family:"Montserrat",sans-serif;
    font-weight:700;font-size:14px;letter-spacing:5px;color:var(--ink);line-height:20px;}
  .title-main{position:absolute;left:690px;top:128px;width:470px;text-align:center;margin:0;
    font-weight:700;font-size:112px;line-height:1;color:var(--ink);letter-spacing:-2px;}
  .title-sub{position:absolute;left:690px;top:246px;width:470px;text-align:center;margin:0;
    font-weight:400;font-size:56px;line-height:1;color:var(--title-blue);letter-spacing:1px;}
  .group-photo{position:absolute;left:672px;top:388px;width:490px;height:330px;
    background:linear-gradient(180deg,#e8e8e8 0%,var(--photo-grey) 50%,#8a8a8a 100%);}
  .subtitle{position:absolute;left:700px;top:494px;margin:0;font-family:"Montserrat",sans-serif;font-weight:700;
    font-size:25px;letter-spacing:1.5px;color:var(--text-dark);}
  .subtitle span{display:block;width:max-content;background:rgba(255,255,255,.85);padding:2px 4px;margin-bottom:6px;line-height:32px;}
  .subtitle em{font-style:normal;color:var(--accent-blue);}
  .name-band{position:absolute;left:636px;top:715px;width:564px;height:35px;background:var(--band-blue);}
  .author-name{position:absolute;left:96px;top:0;line-height:35px;white-space:nowrap;font-family:"Montserrat",sans-serif;font-weight:700;
    font-size:21px;letter-spacing:6px;color:var(--ink);}
  .site{position:absolute;right:16px;top:0;line-height:35px;white-space:nowrap;font-size:9px;color:var(--ink);}
</style>
</head>
<body>
<div class="cover">
  <div class="sky" role="img" aria-label="Soft blue geometric background fading to white"></div>

  <section class="back-cover">
    <div class="author-photo" role="img" aria-label="Black and white portrait of the author with arms crossed"></div>
    <div class="about-label">ABOUT AUTHOR</div>
  </section>

  <section class="spine">
    <div class="spine-title"><b>Sunward</b> <span>Ledger</span></div>
    <div class="spine-author">DORAN PELWICK</div>
  </section>

  <section class="front-cover">
    <h1 class="title-main">Sunward</h1>
    <h2 class="title-sub">LEDGER</h2>
    <div class="group-photo" role="img" aria-label="Black and white photo of six diverse young professionals standing together"></div>
    <p class="subtitle">
      <span>SEVEN <em>QUIET</em></span>
      <span><em>STEPS</em> TOWARD <em>STEADY</em></span>
      <span><em>GROUND</em> AT <em>WORK</em></span>
    </p>
    <div class="name-band">
      <div class="author-name">DORAN PELWICK</div>
      <div class="site">www.doranpelwick.com</div>
    </div>
  </section>
</div>
</body>
</html>
```